Redesign our iOS App Design mockups

- Redesign our current Zelvo App Mockup
- Keep the design simple so that programmers do not have to do too much extra work to make your design work.
- Look at the attached website screenshot for the overall look and feel, and color scheme
- Convert the attached vector logo to iOS Icon format.
- Deliver all graphics in the density required for Zelvo QT Grand.
- I have attached the current iOS mockup in a .ZIP file but you can view it here as well: https://boards.kelmoraview.com/share/TRWQBN8HDK2

Target Market(s)

Mostly Male Internet Consumers between the ages of 20 and 35

Industry/Entity Type

Internet

Colors

Designer to choose colors to be used in the design.

Requirements
Must have
• - Deliver all graphics in the density required for Zelvo QT Grand
• - Should also look good on Murel and Murel pro
• - Design type should be “FLAT.”
• - Spell out fonts used in the design and where they are used. Also, include font sizes.
• - Please use ALL the elements in each page and use all placements and text EXACTLY. Please do not improvise with text or components.
• I have designed the mockup exactly the way I like it. I just want it to made to look better.
Should not have

```html
<!DOCTYPE html>
<html lang="en">
<head>
<meta charset="utf-8">
<title>Hollo VPN – Home</title>
<link rel="stylesheet" href="https://fonts.googleapis.com/css2?family=Inter:wght@400;500;600&family=Montserrat:wght@600;700&display=swap">
<style>
  :root {
    --brand: #f45f4e;
    --brand-deep: #ef5642;
    --screen-bg: #efeff4;
    --ring-outer: #e7e7e7;
    --ring-middle: #d9d9d9;
    --row-bg: #ffffff;
    --divider: #dcdce0;
    --text: #111111;
    --label: #6d6d72;
    --chevron: #c4c4c8;
    --star-off: #c7c7cc;
    --star-on: #ffd60a;
    --white: #ffffff;
  }
  * { margin: 0; padding: 0; box-sizing: border-box; }
  html, body { width: 1200px; height: 3982px; overflow: hidden; }
  body { background: var(--screen-bg); font-family: "Inter", Helvetica, Arial, sans-serif; color: var(--text); position: relative; }

  .app-header { position: absolute; left: 0; top: 0; width: 1200px; height: 279px; background: var(--brand); color: var(--white); }
  .status-time { position: absolute; left: 120px; top: 40px; font-size: 42px; font-weight: 600; }
  .status-icons { position: absolute; right: 40px; top: 48px; }
  .menu-button { position: absolute; left: 42px; top: 172px; }
  .app-title { position: absolute; left: 0; right: 0; top: 168px; text-align: center; font-family: "Montserrat", Arial, sans-serif; font-weight: 700; font-size: 47px; color: #111; }
  .ping-test { position: absolute; right: 28px; top: 124px; width: 150px; text-align: center; font-size: 37px; }
  .ping-test svg { display: block; margin: 0 auto 6px; }

  .connection-status { position: absolute; left: 0; right: 0; top: 386px; text-align: center; font-family: "Montserrat", Arial, sans-serif; font-weight: 600; font-size: 80px; letter-spacing: 1px; color: var(--brand-deep); }
  .connect-dial { position: absolute; left: 0; top: 648px; }

  .section-label { position: absolute; left: 53px; font-size: 35px; color: var(--label); letter-spacing: 1px; }
  .list { position: absolute; left: 0; width: 1200px; background: var(--row-bg); border-top: 2px solid var(--divider); border-bottom: 2px solid var(--divider); }
  .list-row { position: relative; height: 141px; display: flex; align-items: center; font-size: 50px; }
  .list-row + .list-row::before { content: ""; position: absolute; left: 53px; right: 0; top: 0; height: 2px; background: var(--divider); }
  .list-row.is-country + .list-row.is-country::before { left: 0; }
  .row-text { position: absolute; left: 53px; }
  .is-country .row-text { left: 149px; }
  .flag { position: absolute; left: 21px; top: 17px; }
  .star { position: absolute; left: 1036px; top: 41px; }
  .chevron { position: absolute; left: 1140px; top: 50px; }

  .home-indicator { position: absolute; left: 388px; top: 3941px; width: 424px; height: 14px; border-radius: 7px; background: #111; }
</style>
</head>
<body>
<svg width="0" height="0" style="position:absolute">
  <defs>
    <symbol id="chevron" viewBox="0 0 24 40"><path d="M4 4 L20 20 L4 36" fill="none" stroke="var(--chevron)" stroke-width="4" stroke-linecap="round" stroke-linejoin="round"/></symbol>
    <symbol id="star" viewBox="0 0 60 58"><path d="M30 2 L38 21 L58 22 L42 35 L48 55 L30 44 L12 55 L18 35 L2 22 L22 21 Z"/></symbol>
    <clipPath id="flag-clip" clipPathUnits="objectBoundingBox"><circle cx="0.5" cy="0.5" r="0.5"/></clipPath>
    <symbol id="flag-de" viewBox="0 0 106 106"><g clip-path="url(#flag-clip)"><rect width="106" height="36" fill="#111"/><rect y="35" width="106" height="36" fill="#dd0000"/><rect y="70" width="106" height="36" fill="#ffce00"/></g></symbol>
  </defs>
</svg>

<header class="app-header">
  <div class="status-time">9:41</div>
  <svg class="status-icons" width="200" height="36" viewBox="0 0 200 36" aria-hidden="true">
    <g fill="#fff">
      <rect x="0" y="24" width="8" height="10" rx="2"/><rect x="13" y="17" width="8" height="17" rx="2"/><rect x="26" y="10" width="8" height="24" rx="2"/><rect x="39" y="2" width="8" height="32" rx="2"/>
      <path d="M82 32 l-6-7 a10 10 0 0 1 12 0 z"/>
      <path d="M70 18 a18 18 0 0 1 24 0" fill="none" stroke="#fff" stroke-width="5" stroke-linecap="round"/>
      <path d="M63 10 a28 28 0 0 1 38 0" fill="none" stroke="#fff" stroke-width="5" stroke-linecap="round"/>
      <rect x="122" y="4" width="64" height="28" rx="7"/><rect x="189" y="13" width="5" height="10" rx="2"/>
    </g>
  </svg>
  <svg class="menu-button" width="112" height="64" viewBox="0 0 112 64" aria-label="Menu" role="img">
    <g fill="#fff"><rect y="0" width="112" height="10" rx="5"/><rect y="27" width="112" height="10" rx="5"/><rect y="54" width="112" height="10" rx="5"/></g>
  </svg>
  <div class="app-title">Hollo VPN</div>
  <div class="ping-test">
    <svg width="60" height="60" viewBox="0 0 60 60" aria-hidden="true">
      <circle cx="30" cy="30" r="26" fill="none" stroke="#fff" stroke-width="4"/>
      <circle cx="30" cy="17" r="3.5" fill="#fff"/>
      <rect x="27" y="25" width="6" height="20" rx="2" fill="#fff"/>
    </svg>
    Ping Test
  </div>
</header>

<div class="connection-status">NOT CONNECTED</div>

<svg class="connect-dial" width="1200" height="1200" viewBox="0 0 1200 1200" role="img" aria-label="Connect button">
  <defs>
    <linearGradient id="dial-core" x1="0" y1="0" x2="0" y2="1">
      <stop offset="0" stop-color="#ffffff"/><stop offset="1" stop-color="#ececec"/>
    </linearGradient>
  </defs>
  <circle cx="600" cy="600" r="600" fill="var(--ring-outer)"/>
  <circle cx="600" cy="600" r="454" fill="var(--ring-middle)"/>
  <circle cx="600" cy="600" r="289" fill="url(#dial-core)"/>
  <path d="M660 455 L503 650 L590 650 L545 745 L697 560 L612 560 Z" fill="var(--brand)"/>
</svg>

<div class="section-label" style="top:1966px">FAVORITES</div>
<div class="list" style="top:2034px">
  <div class="list-row is-country">
    <svg class="flag" width="106" height="106"><use href="#flag-de"/></svg>
    <span class="row-text">Germany</span>
    <svg class="chevron" width="24" height="40"><use href="#chevron"/></svg>
  </div>
</div>

<div class="section-label" style="top:2250px">SPECIALTY SERVERS</div>
<div class="list" style="top:2316px">
  <div class="list-row"><span class="row-text">Streaming Servers</span><svg class="chevron" width="24" height="40"><use href="#chevron"/></svg></div>
  <div class="list-row"><span class="row-text">P2P Servers</span><svg class="chevron" width="24" height="40"><use href="#chevron"/></svg></div>
  <div class="list-row"><span class="row-text">Onion over VPN</span><svg class="chevron" width="24" height="40"><use href="#chevron"/></svg></div>
</div>

<div class="section-label" style="top:2808px">COUNTRY</div>
<div class="list" style="top:2876px">
  <div class="list-row is-country">
    <svg class="flag" width="106" height="106" viewBox="0 0 106 106" aria-hidden="true"><g clip-path="url(#flag-clip)">
      <rect width="106" height="106" fill="#fff"/>
      <g fill="#d22030"><rect y="0" width="106" height="9"/><rect y="16" width="106" height="9"/><rect y="32" width="106" height="9"/><rect y="48" width="106" height="9"/><rect y="64" width="106" height="9"/><rect y="80" width="106" height="9"/><rect y="96" width="106" height="10"/></g>
      <rect width="50" height="57" fill="#2a3b86"/></g></svg>
    <span class="row-text">USA</span>
    <svg class="star" width="60" height="58" fill="var(--star-off)"><use href="#star"/></svg>
    <svg class="chevron" width="24" height="40"><use href="#chevron"/></svg>
  </div>
  <div class="list-row is-country">
    <svg class="flag" width="106" height="106" viewBox="0 0 106 106" aria-hidden="true"><g clip-path="url(#flag-clip)">
      <rect width="106" height="106" fill="#1f3a8a"/>
      <path d="M0 0 L106 106 M106 0 L0 106" stroke="#fff" stroke-width="18"/>
      <path d="M0 0 L106 106 M106 0 L0 106" stroke="#d22030" stroke-width="6"/>
      <rect x="38" width="30" height="106" fill="#fff"/><rect y="38" width="106" height="30" fill="#fff"/>
      <rect x="45" width="16" height="106" fill="#d22030"/><rect y="45" width="106" height="16" fill="#d22030"/></g></svg>
    <span class="row-text">UK</span>
    <svg class="star" width="60" height="58" fill="var(--star-off)"><use href="#star"/></svg>
    <svg class="chevron" width="24" height="40"><use href="#chevron"/></svg>
  </div>
  <div class="list-row is-country">
    <svg class="flag" width="106" height="106" viewBox="0 0 106 106" aria-hidden="true"><g clip-path="url(#flag-clip)">
      <rect width="106" height="106" fill="#fff"/>
      <path d="M53 26 L60 40 L72 36 L66 56 L76 58 L58 70 L56 82 L50 82 L48 70 L30 58 L40 56 L34 36 L46 40 Z" fill="#e11d2a"/></g></svg>
    <span class="row-text">Canada</span>
    <svg class="star" width="60" height="58" fill="var(--star-off)"><use href="#star"/></svg>
    <svg class="chevron" width="24" height="40"><use href="#chevron"/></svg>
  </div>
  <div class="list-row is-country">
    <svg class="flag" width="106" height="106" viewBox="0 0 106 106" aria-hidden="true"><g clip-path="url(#flag-clip)">
      <rect width="106" height="36" fill="#f7882f"/><rect y="35" width="106" height="36" fill="#fff"/><rect y="70" width="106" height="36" fill="#138808"/>
      <circle cx="53" cy="53" r="11" fill="none" stroke="#1a3a8f" stroke-width="3"/></g></svg>
    <span class="row-text">India</span>
    <svg class="star" width="60" height="58" fill="var(--star-off)"><use href="#star"/></svg>
    <svg class="chevron" width="24" height="40"><use href="#chevron"/></svg>
  </div>
  <div class="list-row is-country">
    <svg class="flag" width="106" height="106" viewBox="0 0 106 106" aria-hidden="true"><g clip-path="url(#flag-clip)">
      <rect width="106" height="36" fill="#e0252b"/><rect y="35" width="106" height="36" fill="#fff"/><rect y="70" width="106" height="36" fill="#1f3f95"/></g></svg>
    <span class="row-text">France</span>
    <svg class="star" width="60" height="58" fill="var(--star-off)"><use href="#star"/></svg>
    <svg class="chevron" width="24" height="40"><use href="#chevron"/></svg>
  </div>
  <div class="list-row is-country">
    <svg class="flag" width="106" height="106" viewBox="0 0 106 106" aria-hidden="true"><g clip-path="url(#flag-clip)">
      <rect width="106" height="53" fill="#e0252b"/><rect y="53" width="106" height="53" fill="#fff"/>
      <circle cx="32" cy="27" r="14" fill="#fff"/><circle cx="37" cy="27" r="13" fill="#e0252b"/></g></svg>
    <span class="row-text">Singapore</span>
    <svg class="star" width="60" height="58" fill="var(--star-off)"><use href="#star"/></svg>
    <svg class="chevron" width="24" height="40"><use href="#chevron"/></svg>
  </div>
  <div class="list-row is-country">
    <svg class="flag" width="106" height="106"><use href="#flag-de"/></svg>
    <span class="row-text">Germany</span>
    <svg class="star" width="60" height="58" fill="var(--star-on)"><use href="#star"/></svg>
    <svg class="chevron" width="24" height="40"><use href="#chevron"/></svg>
  </div>
</div>

<div class="home-indicator"></div>
</body>
</html>
```